Need innovative card design for tech start up

We are a Santa Monica based marketing analytics software start up called Brightwell Metrics. We're launching a platform that will help advertisers better measure and optimize their marketing spend by using advanced algorithmic analytic. While our subject matter is complicated, we want to convey simple, clean, curated. We also want to stand out - ad tech is a sea of sameness and we need to have some individuality. We have an established color palette and would like to see a design we could print in each tone (teal, tangerine, grey), but it doesn't require the card to be monochromatic. The font used is DENSE.

Marketing

```html
<!DOCTYPE html>
<html lang="en">
<head>
<meta charset="utf-8">
<title>Brightwell Metrics — Business Card</title>
<link rel="stylesheet" href="https://fonts.googleapis.com/css2?family=Oswald:wght@300;400;500&display=swap">
<style>
  :root {
    --backdrop: #e6e4e1;
    --charcoal: #2f3133;
    --tangerine: #f28c28;
    --paper: #ffffff;
    --grey-text: #8a8c8e;
    --light-text: #f2f2f2;
    --ink: #1e1e1e;
  }
  * { box-sizing: border-box; margin: 0; padding: 0; }
  html, body {
    width: 1200px; height: 1000px; overflow: hidden;
    background: var(--backdrop);
    font-family: "Oswald", sans-serif;
  }
  .stage { position: relative; width: 1200px; height: 1000px; }

  .card {
    position: absolute; top: 150px;
    width: 400px; height: 700px;
    overflow: hidden;
    box-shadow: 0 8px 24px rgba(0,0,0,0.18);
  }
  .card--front { left: 150px; background: var(--charcoal); }
  .card--back { left: 650px; background: var(--paper); }

  /* brand block */
  .brand-square { position: absolute; background: var(--tangerine); }
  .card--front .brand-square { left: 80px; top: 150px; width: 240px; height: 240px; }
  .card--back .brand-square { left: 105px; top: 60px; width: 190px; height: 190px; }

  .brand-name {
    position: absolute; left: 0; width: 100%;
    text-align: center; text-transform: uppercase;
    font-weight: 300; letter-spacing: 0.5px;
    color: var(--grey-text);
    white-space: nowrap;
  }
  .card--front .brand-name { top: 405px; font-size: 32px; }
  .card--back .brand-name { top: 262px; font-size: 24px; }

  /* back: name band */
  .name-band {
    position: absolute; left: 0; top: 330px; width: 100%; height: 95px;
    background: var(--tangerine);
    padding: 26px 0 0 40px;
    color: var(--ink);
  }
  .person-name { font-size: 28px; font-weight: 500; letter-spacing: 1px; line-height: 1.1; }
  .person-title { font-size: 18px; font-weight: 400; letter-spacing: 1px; line-height: 1.3; }

  /* back: contact panel */
  .contact-panel {
    position: absolute; left: 0; top: 425px; width: 100%; height: 275px;
    background: var(--charcoal);
    padding: 28px 0 0 40px;
    color: var(--light-text);
    font-weight: 300; font-size: 19px; letter-spacing: 1.2px; line-height: 1.3;
    white-space: nowrap;
  }
  .address { margin-bottom: 46px; }
</style>
</head>
<body>
<main class="stage">
  <section class="card card--front" aria-label="Card front">
    <div class="brand-square"></div>
    <p class="brand-name">Brightwell Metrics</p>
  </section>

  <section class="card card--back" aria-label="Card back">
    <div class="brand-square"></div>
    <p class="brand-name">Brightwell Metrics</p>

    <div class="name-band">
      <p class="person-name">Daniel Marwick</p>
      <p class="person-title">Founder/CEO</p>
    </div>

    <div class="contact-panel">
      <p class="address">1480 Harbor Lane, Suite 300<br>Santa Monica, CA 90401</p>
      <p class="contacts">
        Phone: 310-555-0142 x101<br>
        Mobile: 310-555-0187<br>
        Email: daniel@brightwellmetrics.com<br>
        Website: www.brightwellmetrics.com
      </p>
    </div>
  </section>
</main>
</body>
</html>
```